Business card design needed

We are 2 artists starting up a studio by the water in Sydney ...where we can work and display our art...would like the back ground to be Navy and white stripe...nautical...and the name The Clay Nook to be bold and the main wording...not nautical...if possible thought the A for art could be an easel ...ie the capital A using the cross bar as the platform that paint would be circles of colour....would like the main wording in Black but the easel A in colour
Hope u are able to help
thanku Lorna Vesk
as I will be away in a week for 4 weeks could u please send all info to Jodie Minchens email....she can contact me and we can go ahead asap....

Industry/Entity Type

Artists

Contact Information for Business Card

THE CLAY NOOK

Halloways Dock House
The Bend..41 Kelvane Rd..Mosman 2088 Sydney

Jodi Minchen..0417583091..jodiminchen@mailwave.example
Lorn Vesk...0413862714..lvesk@quillnet.example.au

```html
<!DOCTYPE html>
<html lang="en">
<head>
<meta charset="utf-8">
<title>The Clay Nook — Business Card</title>
<link rel="stylesheet" href="https://fonts.googleapis.com/css2?family=Questrial&display=swap">
<style>
  :root {
    --page: #ffffff;
    --navy: #0b3a5c;
    --ink: #ffffff;
  }
  html, body {
    margin: 0;
    padding: 0;
    width: 1200px;
    height: 1000px;
    overflow: hidden;
    background: var(--page);
  }
  .canvas {
    position: relative;
    width: 1200px;
    height: 1000px;
  }
  .card {
    position: absolute;
    left: 386px;
    top: 138px;
    width: 428px;
    height: 750px;
    background: var(--navy);
    color: var(--ink);
    font-family: "Questrial", "Century Gothic", sans-serif;
    text-align: center;
  }
  .card-frame {
    position: absolute;
    inset: 0;
  }
  .studio-name {
    position: absolute;
    left: 0;
    right: 0;
    top: 78px;
    margin: 0;
    font-weight: 400;
    line-height: 1;
  }
  .studio-name .line-the {
    display: block;
    font-size: 54px;
  }
  .studio-name .line-main {
    display: block;
    font-size: 62px;
    margin-top: 14px;
  }
  .address {
    position: absolute;
    left: 0;
    right: 0;
    top: 292px;
    margin: 0;
    font-size: 17px;
    line-height: 22.5px;
    letter-spacing: 0.3px;
    text-transform: uppercase;
    font-style: normal;
  }
  .stars {
    position: absolute;
    left: 0;
    top: 418px;
  }
  .contacts {
    position: absolute;
    left: 0;
    right: 0;
    top: 517px;
  }
  .contact {
    margin: 0 0 22px;
    font-size: 17.5px;
    line-height: 22.5px;
    letter-spacing: 0.4px;
  }
  .contact span { display: block; }
</style>
</head>
<body>
<div class="canvas">
  <section class="card">
    <svg class="card-frame" width="428" height="750" viewBox="0 0 428 750" aria-hidden="true">
      <rect x="25.5" y="24.5" width="377" height="706" fill="none" stroke="#ffffff" stroke-width="3" stroke-dasharray="28 18"/>
    </svg>

    <h1 class="studio-name">
      <span class="line-the">The</span>
      <span class="line-main">Clay Nook</span>
    </h1>

    <address class="address">
      Halloways Dock House<br>
      The Bend<br>
      41 Kelvane Rd • Mosman • 2088<br>
      Sydney
    </address>

    <svg class="stars" width="428" height="60" viewBox="0 0 428 60" aria-hidden="true">
      <polygon fill="#ffffff" transform="translate(150 27) scale(16)" points="0,-1 0.2245,-0.309 0.951,-0.309 0.363,0.118 0.588,0.809 0,0.382 -0.588,0.809 -0.363,0.118 -0.951,-0.309 -0.2245,-0.309"/>
      <polygon fill="#ffffff" transform="translate(221 29) scale(25)" points="0,-1 0.2245,-0.309 0.951,-0.309 0.363,0.118 0.588,0.809 0,0.382 -0.588,0.809 -0.363,0.118 -0.951,-0.309 -0.2245,-0.309"/>
      <polygon fill="#ffffff" transform="translate(293 27) scale(16)" points="0,-1 0.2245,-0.309 0.951,-0.309 0.363,0.118 0.588,0.809 0,0.382 -0.588,0.809 -0.363,0.118 -0.951,-0.309 -0.2245,-0.309"/>
    </svg>

    <div class="contacts">
      <p class="contact">
        <span class="contact-name">Jodi Minchen</span>
        <span class="contact-phone">0417583091</span>
        <span class="contact-email">jodiminchen@mailwave.example</span>
      </p>
      <p class="contact">
        <span class="contact-name">Lorn Vesk</span>
        <span class="contact-phone">0413862714</span>
        <span class="contact-email">lvesk@quillnet.example.au</span>
      </p>
    </div>
  </section>
</div>
</body>
</html>
```